Web Redesign

Hi,
We have a created a webpage on pagemill using a theme called Quorvel which can be downloaded at Skin Pantry which we like the look and feel of.

You can view our current page we are building at:: www.tillbrookhelp.com.au

The text needs altering which we will do ourselves. Basically, we are requiring the graphic elements that should be placed on EACh page.

The webpage we like the look and feel of is:
http://www.moonlark.com.au/
http://www.codevix.com.au/

Ideas for pages:
Our process - could be something along the lines of http://www.codevix.com.au/our-method
Our service - could be something along the lines of http://www.moonlark.com.au/iphone-application-development/
Our work - could be something along the lines of http://www.codevix.com.au/our-work
Our Value Proposition - could be something along hte lines of http://www.moonlark.com.au/services/
About Us - happy to go with your suggestion
Contact us - happy to use what we have currently if you can come up with a suitable graphic http://tillbrookhelp.com.au/contact-example-1/
FAQ - happy to use what we have currently if you can come up with a suitable graphic http://tillbrookhelp.com.au/contact-example-1/

We would like you to come up with the design/graphics and add then once the winner of the project is chosen we could give you the admin login details to upload the images or we could do it ourselves if you supplied them all and in which case would be good to know where you envision they would be placed.

To give you some insight, this is a branch from business we have called HandBolt (www.handbolt.org) where we aggregate charities onto the one platform for smart phones and allow people to donate to their favourite charity anywhere, anytime with the push of a button.
Tillbrookhelp is a side business to this where we have began building white labelled Tillbrook Help on our HandBolt platform and we wanted a separate webpage for this.

Once this webpage is completed, we would love to get the HandBolt webpage revamped so there is further opportunity to work with you on this project.

Happy to answer any questions if needed.

Thanks and look forward to seeing the designs

Our Ideas for pages:

Target Market(s)

Charities, corporates

Industry/Entity Type

Building

```html
<!DOCTYPE html>
<html lang="en">
<head>
<meta charset="utf-8">
<title>Tillbrook Help</title>
<link rel="stylesheet" href="https://fonts.googleapis.com/css2?family=Open+Sans:wght@400;600;700&family=Archivo+Narrow&family=Tinos&display=swap">
<style>
:root{
  --brown:#3a1c10;
  --brown-mid:#5b2112;
  --orange:#f39322;
  --orange-light:#f8a640;
  --green:#1d7a22;
  --green-dark:#0f5a16;
  --text:#444;
  --muted:#8a8a8a;
  --page:#efefef;
  --footer:#2a2a2a;
  --footer-text:#6f6f6f;
  --white:#fff;
}
*{box-sizing:border-box;margin:0;padding:0}
html,body{width:745px;height:1200px;overflow:hidden}
body{position:relative;font-family:"Open Sans",sans-serif;background:var(--page);color:var(--text)}
.abs{position:absolute}
.header{left:0;top:0;width:745px;height:66px;background:linear-gradient(#fff,#f3f3f3)}
.brand{left:100px;top:8px;display:flex;align-items:center;gap:6px}
.brand-mark{width:16px;height:16px;background:var(--brown-mid);border-radius:3px}
.brand-name{font-size:17px;font-weight:600;color:var(--green)}
.top-email{left:390px;top:24px;font-size:8px;color:var(--green)}
.search{left:527px;top:19px;width:130px;height:17px;background:var(--brown);border-radius:2px;font-size:7px;font-style:italic;color:#b99;padding:4px 6px}
.hero{left:0;top:66px;width:745px;height:298px;background:radial-gradient(ellipse at 50% 45%,var(--orange-light),var(--orange) 70%,#ee8418)}
.nav{left:97px;top:53px;width:560px;height:31px;background:linear-gradient(#4a2415,var(--brown));display:flex;border-radius:2px;z-index:2}
.nav-item{color:#fff;font-size:8px;font-weight:700;display:flex;align-items:center;gap:5px;padding:0 14px;border-right:1px solid #6b3a27;height:100%}
.nav-ico{width:8px;height:8px;background:#fff;border-radius:1px;opacity:.9}
.nav-social{margin-left:auto;display:flex;gap:5px;align-items:center;padding-right:9px}
.nav-social span{width:14px;height:14px;background:#fff;border-radius:2px}
.arrow{width:20px;height:20px;background:#fff;top:195px}
.device-art{left:120px;top:130px;width:270px;height:192px;border-radius:6px;background:linear-gradient(135deg,#2a2a2a,#1e5a23 55%,#cfcfcf)}
.hero-title{left:412px;top:161px;font-size:17px;font-weight:700;color:#fff;line-height:22px}
.hero-box{left:411px;width:218px;height:26px;background:#fff;font-size:14px;font-weight:700;color:#555;text-align:center;line-height:26px}
.tagline{left:92px;top:380px;font-size:13px;color:#444}
.tagsub{left:92px;top:397px;font-size:10px;color:#555}
.learn{left:459px;top:383px;width:142px;height:25px;background:linear-gradient(#2c9a2f,var(--green-dark));border-radius:2px;color:#fff;font-size:11px;display:flex;align-items:center;justify-content:center;gap:18px}
.learn i{width:10px;height:10px;border-radius:50%;background:#17331a}
.feature{top:450px;width:130px;text-align:center}
.feature-ico{width:36px;height:36px;border-radius:50%;background:var(--brown-mid);margin:0 auto 12px}
.feature h3{font-size:11.5px;font-weight:400;color:var(--green);line-height:12px;height:26px;display:flex;align-items:flex-end;justify-content:center}
.feature p{font-size:7px;color:var(--muted);line-height:13px;margin-top:6px}
.read{display:inline-block;margin-top:9px;width:43px;height:20px;background:linear-gradient(#ddd,#aaa);border:1px solid #999;font-family:"Tinos",serif;font-size:7px;line-height:18px;color:#333}
.dot{top:626px;width:18px;height:4px;background:var(--brown-mid)}
.section-title{font-size:12.5px;font-weight:600;color:var(--green)}
.card{top:678px;width:131px;height:120px;background:#fff}
.card-img{height:85px}
.card h4{font-size:8.5px;font-weight:700;color:#444;margin:5px 0 0 10px}
.card small{display:block;font-size:7px;color:var(--muted);margin:3px 0 0 10px}
.charities{left:82px;top:838px;width:583px;height:32px;background:#e6e6e6;display:flex;align-items:center;gap:28px;padding-left:7px;white-space:nowrap;overflow:hidden;font-family:"Archivo Narrow",sans-serif;font-size:9px;color:#333}
.charities strong{font-weight:400;font-size:11px}
.press{left:82px;top:908px;width:583px;height:42px;background:#fff;display:flex;align-items:center;justify-content:space-around;font-size:13px;font-weight:700;color:#1c5a99}
.footer{left:0;top:978px;width:745px;height:189px;background:var(--footer)}
.fcol{top:998px;width:131px}
.fcol h5{font-size:10.5px;font-weight:400;color:#bbb;padding-bottom:4px;border-bottom:1px solid #444}
.fcol p{font-size:6.4px;line-height:11.3px;color:var(--footer-text);margin-top:10px}
.fcol p b{color:#ccc;font-weight:400}
.fsocial{display:flex;gap:6px;margin-top:10px}
.fsocial span{width:10px;height:10px;border-radius:50%;background:#777}
.bottom{left:0;top:1167px;width:745px;height:33px;background:var(--green-dark);color:#fff;font-size:7px;display:flex;align-items:center;justify-content:space-between;padding:0 86px}
</style>
</head>
<body>
<div class="abs header"></div>
<div class="abs brand"><span class="brand-mark"></span><span class="brand-name">Tillbrook Help</span></div>
<div class="abs top-email">✉ info@tillbrookhelp.com.au</div>
<div class="abs search">enter your keyword</div>

<div class="abs hero"></div>
<nav class="abs nav">
  <div class="nav-item"><span class="nav-ico"></span>HOME</div>
  <div class="nav-item"><span class="nav-ico"></span>ABOUT US</div>
  <div class="nav-item"><span class="nav-ico"></span>SOLUTIONS</div>
  <div class="nav-item"><span class="nav-ico"></span>PORTFOLIO</div>
  <div class="nav-item" style="border-right:0"><span class="nav-ico"></span>CONTACT US</div>
  <div class="nav-social"><span></span><span></span><span></span></div>
</nav>
<svg class="abs arrow" style="left:81px" viewBox="0 0 20 20"><rect width="20" height="20" fill="#fff"/><path d="M12 6 7 10l5 4z" fill="#222"/></svg>
<svg class="abs arrow" style="left:648px" viewBox="0 0 20 20"><rect width="20" height="20" fill="#fff"/><path d="M8 6l5 4-5 4z" fill="#222"/></svg>
<div class="abs device-art" role="img" aria-label="Desktop monitor and tablet showing the Tillbrook Help website"></div>
<div class="abs hero-title">YOU NEED A WHITE LABEL<br>APP LEAVE IT TO US</div>
<div class="abs hero-box" style="top:211px">WE KNOW ABOUT</div>
<div class="abs hero-box" style="top:241px">NOT-FOR-PROFITS.</div>

<div class="abs tagline">ON TIME. ON BUDGET. WE KNOW ABOUT NOT-FOR-PROFITS.</div>
<div class="abs tagsub">Now is the time to move to mobile fundraising. We can help. Right now.</div>
<div class="abs learn">Learn More... <i></i></div>

<div class="abs feature" style="left:86px"><div class="feature-ico"></div><h3>App Branded With<br>Your Name</h3><p>Donec dui ligula, dictum nec dictum quis, vulputate venenatis augue. Donec dignissim vestibulum leo, non dignissimt.</p><span class="read">Read more</span></div>
<div class="abs feature" style="left:229px"><div class="feature-ico"></div><h3>Receive Donations</h3><p>Donec dui ligula, dictum nec dictum quis, vulputate venenatis augue. Donec dignissim vestibulum leo, non dignissimt.</p><span class="read">Read more</span></div>
<div class="abs feature" style="left:372px"><div class="feature-ico"></div><h3>Contents in your<br>Control</h3><p>Donec dui ligula, dictum nec dictum quis, vulputate venenatis augue. Donec dignissim vestibulum leo, non dignissimt.</p><span class="read">Read more</span></div>
<div class="abs feature" style="left:515px"><div class="feature-ico"></div><h3>Mount Campaign<br>in Seconds</h3><p>Donec dui ligula, dictum nec dictum quis, vulputate venenatis augue. Donec dignissim vestibulum leo, non dignissimt.</p><span class="read">Read more</span></div>
<div class="abs dot" style="left:344px"></div>
<div class="abs dot" style="left:368px;background:var(--green)"></div>
<div class="abs dot" style="left:392px"></div>

<div class="abs section-title" style="left:94px;top:651px">Our Recent Projects</div>
<div class="abs card" style="left:92px"><div class="card-img" role="img" aria-label="Featured project app screen" style="background:linear-gradient(#7d8ea8 0 14px,#e9e3da 14px,#d9453b)"></div><h4>Duis rhoncus odio nec</h4><small>Donec felis diam</small></div>
<div class="abs card" style="left:235px"><div class="card-img" role="img" aria-label="Thank you for giving screen with green tick" style="background:linear-gradient(#e4e7ea,#d6dadd)"></div><h4>In fringilla suscipit</h4><small>Felis malesuada fermentum</small></div>
<div class="abs card" style="left:378px"><div class="card-img" role="img" aria-label="Donation amount buttons" style="background:linear-gradient(#3a8fd0,#1f6fb5)"></div><h4>Vivamus tristique</h4><small>Quisque vitae faucibus leo</small></div>
<div class="abs card" style="left:521px"><div class="card-img" role="img" aria-label="List of charities in the app" style="background:linear-gradient(#f5f5f5,#dcdcdc)"></div><h4>Duis in nisl neque</h4><small>Aenean justo augue</small></div>

<div class="abs charities"><strong>Supported Charities:</strong><span>und</span><span>Harbourlight Aid Australia</span><span>Chronic Pain Support Circle</span><span>KINDRA</span><span>Cure Research Trust Foundation</span></div>
<div class="abs section-title" style="left:89px;top:885px">As Featured In</div>
<div class="abs press"><span>The Meridian</span><span>Harbour Herald</span><span>Ledger Review</span><span>Civic Bono</span><span>Skyline Business</span></div>

<div class="abs footer"></div>
<div class="abs fcol" style="left:92px"><h5>Testimonial</h5><p>Just a quick note to let you know how happy I am with our new e-commerce site. It's working beautifully and handling our holiday sales with ease. The build was simple, painless and the results speak for themselves.<br><b>Daniel Harwick</b><br><b>Marlow's Catalog of Boats and Tide</b></p></div>
<div class="abs fcol" style="left:235px"><h5>Latest tweets</h5><p><b>about 10 days ago</b> I was looking at Business, Portfolio Template / and find elm city web great @tillbrookhelp</p><p style="border-top:1px solid #444;padding-top:12px;margin-top:14px"><b>about 10 days ago</b> I was looking at Business, Portfolio Template / and find elm city web great @tillbrookhelp</p></div>
<div class="abs fcol" style="left:378px"><h5>Contact us</h5><p><b>Tillbrook Help</b><br><b>Abc Eve</b><br>Monday-Friday 9-5pm</p><p>☎ &nbsp;123-555-0190</p><p style="margin-top:4px">✉ &nbsp;<b>info@tillbrookhelp.com.au</b></p></div>
<div class="abs fcol" style="left:521px"><h5>Follow us</h5><div class="fsocial"><span></span><span></span><span></span><span></span><span></span><span></span><span></span></div><p style="margin-top:4px;font-size:7px;line-height:12.5px">Lorem ipsum dolor sit amet, consectetur adipiscing elit. Nunc sed lectus in turpis consequat pharetra. Nulla velit purus, vestibulum sit amet ultrices eget, ultricies ut massa. Cras ac nulla at arcu vehicula hendrerit.</p></div>
<div class="abs bottom"><span>Home | About Us | Solutions | Portfolio | Contact Us</span><span>Copyright © 2004-2013 All Rights Reserved</span></div>
</body>
</html>
```